Anzeigengestaltung für Online-Handel mit Edelmetallen
Zielgruppe
Online Handel mit Edelmetallen wie Gold und Silberbarren und Münzen.
Sowie der Ankauf von Gold per Postankauf
Aufgabenstellung
Ich möchte in verschiedenen Tageszeitungen in Deutschland Werbung schalten . Kleine Anzeigen etwas kleiner als Visitenkarten Größe wegen den Kosten.
Logo
Ihr Onlineshop für Edelmetalle
Vergleichen sie unsere Preis
Goldbarren / Falkenthaler
Shop.Wertkontorlo.de

```html
<!DOCTYPE html>
<html lang="de">
<head>
<meta charset="utf-8">
<title>Wertkontor-Lo.de – Anzeige</title>
<link rel="stylesheet" href="https://fonts.googleapis.com/css2?family=Archivo:wdth,wght@62..125,700&family=Kaushan+Script&family=Poppins:wght@300;400&display=swap">
<style>
  :root {
    --page: #f2f1ef;
    --card: #444444;
    --gold: #d4a24c;
    --white: #ffffff;
    --bar-light: #f7d35a;
    --bar-mid: #d99a1e;
    --bar-dark: #7a4a16;
  }
  * { margin: 0; padding: 0; box-sizing: border-box; }
  html, body {
    width: 1200px; height: 864px; overflow: hidden;
    background: var(--page);
  }
  .ad {
    position: absolute; left: 84px; top: 99px;
    width: 1033px; height: 668px;
    background: var(--card);
    overflow: hidden;
    font-family: "Poppins", sans-serif;
    color: var(--white);
  }
  .headline-ihr {
    position: absolute; left: 80px; top: 80px;
    font-size: 86px; font-weight: 400; line-height: 1;
  }
  .headline-script {
    position: absolute; left: 76px; top: 170px;
    width: 470px; text-align: left;
    font-family: "Kaushan Script", cursive;
    font-size: 92px; line-height: 1.25;
    letter-spacing: -3px;
    white-space: nowrap;
    transform: rotate(-2deg);
    transform-origin: left center;
  }
  .headline-sub {
    position: absolute; left: 94px; top: 300px;
    font-size: 51px; font-weight: 400; line-height: 1;
  }
  .shop-link {
    position: absolute; left: 59px; top: 426px;
    width: 439px; height: 61px;
  }
  .shop-link svg { position: absolute; inset: 0; }
  .shop-link span {
    position: absolute; left: 20px; top: 0; line-height: 61px;
    font-size: 28px; font-weight: 400;
  }
  .brand {
    position: absolute; left: 670px; top: 136px;
    width: 320px; text-align: center;
    font-size: 34px; font-weight: 300; letter-spacing: 0.3px;
  }
  .product-photo {
    position: absolute; left: 519px; top: 221px;
    width: 482px; height: 363px;
    background:
      radial-gradient(ellipse at 40% 35%, var(--bar-light) 0%, var(--bar-mid) 45%, var(--bar-dark) 80%, transparent 100%);
    border-radius: 40px;
    opacity: 0.9;
  }
  .claim-band {
    position: absolute; left: 0; bottom: 0;
    width: 100%; height: 67px;
    background: var(--gold);
    display: flex; align-items: center; justify-content: center;
  }
  .claim-band p {
    font-family: "Archivo", sans-serif;
    font-stretch: 125%;
    font-variation-settings: "wdth" 125;
    font-weight: 700;
    font-size: 34px; color: var(--white);
    letter-spacing: 1.5px;
  }
</style>
</head>
<body>
  <div class="ad">
    <div class="headline-ihr">Ihr</div>
    <div class="headline-script">Onlineshop</div>
    <div class="headline-sub">für Edelmetalle</div>

    <div class="shop-link">
      <svg width="439" height="61" viewBox="0 0 439 61" aria-hidden="true">
        <polygon points="15,2 437,2 437,44 419,59 2,59 2,16" fill="none" stroke="var(--gold)" stroke-width="3"/>
      </svg>
      <span>Shop.Wertkontorlo.de</span>
    </div>

    <div class="brand">Wertkontor-Lo.de</div>

    <div class="product-photo" role="img" aria-label="Foto zweier gekreuzt liegender Goldbarren (Feingold 999,9)"></div>

    <div class="claim-band"><p>Vergleichen sie unsere Preis!</p></div>
  </div>
</body>
</html>
```